依頼詳細
11回目を迎える臨床データ博&ソリューション見本市のA4(4C/1C)チラシの制作をお願い致します。

■制作目的
第11回 臨床データ博&ソリューション見本市 2017 の周知のためのチラシ制作
過去10回行ってきたが11回ということで、デザインを刷新したい。

※臨床データ博、ソリューション見本市について
中堅から大手のメーカーの医療系システムが一同に集まり展示会をするというのは業界的に珍しい為、毎回大盛況です。
医療従事者、病院勤務のシステム管理責任者が来場し最新の医療システムを【見て、知って、触って】頂きます。
各メーカーの担当者も多数いるため、その場で疑問点や導入までのフローなどの気になった点があってもその場で解決できます。
また、同日開催のセミナーを目的として来場される方も多々いらっしゃいます。
上記の二点がこのフェアにお越し頂くお客様の目的になります。

■来場者(配布する方)
医療従事者、病院勤務のシステム管理責任者
実際手に取って見ていただく方は30中頃~の医療従事者になります。

■デザインについて
過去使用されていたものを添付しております。
過去のものでご参考にして頂きたい点は情報の部分のみで、大幅にデザインを刷新するのでポップなものや厳格なもの幅広いイメージでご提案頂けると幸いです。

※重要
三つ折りにした際に
タイトル/日時/セミナーが折り目と被らないようにお願い致します。

■チラシのお渡し方法
チラシは三つ折りにして透明のポリ封筒にいれて発送、もしくは営業担当者が直接手渡ししてお渡しします。

定期的に同様のフェアなどの案内がありますので継続してお付き合い頂ける方にお願いできればと思います。

記載項目
・表面(4C)
●必須記載事項
①タイトル
臨床データ博 2017
第11回 臨床データ博&ソリューション見本市
②日時
2017年8月〇日(〇)
開催時間 13:00~17:30[受付開始12:30~]
展示会場 グランフォレスト迎賓館福岡
[福岡市博多区竹下緑町5-8-3]
③参加料無料
④キャッチコピー
医療・介護 そして、地域連携をささえるソリューションが一同に展示
⑤主催
株式会社 ミナトラボ
⑥セミナー情報
タイトル/講師/講演時間/会場
※上記記載情報は後程お送りいたしますのでダミーでお願いします。

・裏面(1C)
裏面のデータは毎年使用しているテンプレに沿った形で制作お願いしたいと思っ  ておりますので、流し込みの作業をお願いしますので取り急ぎ表面のみでご提案  お願い致します。
※昨年と出展企業に変更なければデザイン変更はありません。

サイズ
A4
ページ数
両面
希望イメージ
シンプル 複雑
単色 カラフル
暗い 明るい
日常 高級
遊び心 厳粛
未来的 伝統的
女性的 男性的
希望する色
黄・オレンジ系、医療従事者向けのフェアですのでPOPすぎないようにお願い致します。
納品ファイル
• イラストレーター形式 (.ai)
補足説明
参考資料添付しております。
■ 選んだ理由

情報が整理され見やすいレイアウトが大変気に入りました。

■ 提案者全員のお礼・コメント

素晴らしいご提案ありがとうございました。

```html
<!DOCTYPE html>
<html lang="ja">
<head>
<meta charset="UTF-8">
<title>第11回 臨床データ博&amp;ソリューション見本市 2017</title>
<link href="https://fonts.googleapis.com/css2?family=Noto+Sans+JP:wght@400;500;700;900&family=Noto+Serif+JP:wght@700;900&display=swap" rel="stylesheet">
<style>
  :root{
    --orange:#ee7d1c;
    --orange-deep:#d9620f;
    --amber:#f6a623;
    --yellow:#fbd24a;
    --cream:#fff6dc;
    --ink:#3a2a1a;
    --white:#ffffff;
    --photo-light:#eceef0;
    --photo-mid:#c9ced4;
  }
  *{box-sizing:border-box;margin:0;padding:0}
  html,body{width:857px;height:1200px;overflow:hidden;background:#fff}
  body{font-family:"Noto Sans JP",sans-serif;color:var(--ink)}
  .flyer{position:relative;width:857px;height:1200px;overflow:hidden;
    background:linear-gradient(180deg,var(--white) 0,var(--white) 560px,var(--yellow) 660px,var(--amber) 860px,var(--orange) 1110px,var(--white) 1110px)}
  .hero-photo{position:absolute;left:0;top:0;width:857px;height:670px;
    background:linear-gradient(180deg,var(--photo-light) 0%,#f4f4f5 30%,var(--photo-mid) 55%,#fbe3b0 82%,rgba(251,210,74,0) 100%)}
  .title-band{position:absolute;left:0;top:22px;height:66px;padding:0 28px 0 22px;
    background:var(--orange);color:#fff;font-family:"Noto Serif JP",serif;font-weight:900;
    font-size:44px;line-height:66px;letter-spacing:2px;white-space:nowrap}
  .subtitle-band{position:absolute;left:0;top:88px;height:62px;padding:0 24px 0 22px;
    background:rgba(255,255,255,.92);color:var(--orange-deep);font-family:"Noto Serif JP",serif;
    font-weight:900;font-size:38px;line-height:62px;white-space:nowrap}
  .catch-copy{position:absolute;right:24px;top:175px;width:250px;transform:rotate(-8deg);
    color:var(--orange-deep);font-weight:700;font-size:19px;line-height:1.6;text-align:center}
  .free-badge{position:absolute;left:30px;top:515px;width:104px;height:104px;border-radius:50%;
    background:rgba(255,255,255,.85);border:3px solid var(--orange);color:var(--orange-deep);
    display:flex;align-items:center;justify-content:center;text-align:center;font-weight:700;font-size:21px;line-height:1.25}
  .info-row{position:absolute;left:28px;display:flex;align-items:center;gap:16px}
  .label{background:var(--orange-deep);color:#fff;font-weight:700;font-size:19px;
    width:104px;height:46px;display:flex;align-items:center;justify-content:center;flex:none}
  .date{top:678px}
  .date-value{font-weight:900;font-size:30px;color:var(--ink)}
  .date-value .big{font-size:58px;line-height:1;color:var(--orange-deep)}
  .time{left:470px;top:690px;display:flex;gap:16px;align-items:center;position:absolute}
  .time-value{font-weight:700;font-size:22px;line-height:1.3}
  .venue{top:768px;align-items:flex-start}
  .venue-value{font-weight:700;font-size:22px;line-height:1.4}
  .host{left:470px;top:768px;position:absolute;display:flex;gap:16px;align-items:flex-start}
  .host-value{font-weight:900;font-size:26px;line-height:1.3}
  .seminar{position:absolute;left:20px;top:860px;width:817px;height:240px;background:var(--cream);
    display:flex;gap:24px;padding:18px 20px}
  .seminar-col{flex:1;position:relative}
  .tag{display:inline-block;background:var(--orange);color:#fff;font-weight:700;font-size:15px;padding:3px 12px;margin-bottom:6px}
  .seminar-title{font-weight:900;font-size:21px;color:var(--orange-deep);margin-bottom:4px}
  .dummy{font-size:13px;line-height:1.5;color:var(--ink);margin-bottom:10px}
  .dummy-large{font-size:19px;font-weight:700;color:var(--orange-deep)}
  .speaker{display:flex;align-items:center;gap:10px;margin-top:4px}
  .speaker-name{font-weight:700;font-size:19px;color:var(--orange-deep)}
  .speaker-photo{position:absolute;right:0;bottom:0;width:120px;height:120px;background:#fff;border:1px solid #e2cfa8}
  .contact{position:absolute;left:0;top:1110px;width:857px;height:90px;background:#fff;display:flex;align-items:center;padding:0 24px}
  .phones{color:var(--orange-deep);font-weight:900}
  .phone{font-size:36px;line-height:1.05;display:flex;align-items:center;gap:8px}
  .fax{font-size:28px;line-height:1.1}
  .org{margin-left:auto;font-weight:700;font-size:20px;color:var(--ink);line-height:1.35}
  .org small{display:block;font-size:13px;font-weight:500}
  .org-mark{width:60px;height:60px;background:var(--orange);margin-left:18px;flex:none}
</style>
</head>
<body>
<main class="flyer">
  <div class="hero-photo" role="img" aria-label="白衣に聴診器を掛けた医師が赤いハートを手に持つ写真(顔は画面外)"></div>

  <h1 class="title-band">第11回 臨床データ博 2017</h1>
  <p class="subtitle-band">臨床データ博&amp;ソリューション見本市</p>

  <p class="catch-copy">医療・介護 そして、地域連携を<br>ささえるソリューションが<br>一同に展示</p>

  <div class="free-badge">参加料<br>無料</div>

  <div class="info-row date">
    <span class="label">開催日時</span>
    <span class="date-value">2017年<span class="big">8</span>月<span class="big">12</span>日(土)</span>
  </div>
  <div class="time">
    <span class="label">開催時間</span>
    <span class="time-value">13:00~17:30<br>受付開始 12:30~</span>
  </div>

  <div class="info-row venue">
    <span class="label">展示会場</span>
    <span class="venue-value">グランフォレスト迎賓館福岡<br>福岡市博多区竹下緑町5-8-3</span>
  </div>
  <div class="host">
    <span class="label">主 催</span>
    <span class="host-value">株式会社<br>ミナトラボ</span>
  </div>

  <section class="seminar">
    <div class="seminar-col">
      <span class="tag">講演タイトル</span>
      <p class="seminar-title">「ここに講演タイトルが入ります。」</p>
      <p class="dummy">この文章はダミーです。文字の大きさ、量、字間、行間等を確認するために入れています。</p>
      <span class="tag">講演会場</span>
      <p class="dummy dummy-large">この文章はダミーです。文字の</p>
    </div>
    <div class="seminar-col">
      <span class="tag">講演スケジュール</span>
      <p class="dummy dummy-large">この文章はダミーです。文字の</p>
      <p class="dummy" style="width:230px">この文章はダミーです。文字の大きさ、量、字間を確認します。</p>
      <div class="speaker"><span class="tag" style="margin:0">講師</span><span class="speaker-name">講師名が入ります</span></div>
      <div class="speaker-photo" role="img" aria-label="講師の写真が入るスペース"></div>
    </div>
  </section>

  <footer class="contact">
    <div class="phones">
      <p class="phone">
        <svg width="30" height="30" viewBox="0 0 24 24" aria-hidden="true"><path fill="#d9620f" d="M6.6 10.8a15 15 0 0 0 6.6 6.6l2.2-2.2a1 1 0 0 1 1-.25 11.4 11.4 0 0 0 3.6.57 1 1 0 0 1 1 1V20a1 1 0 0 1-1 1A17 17 0 0 1 3 4a1 1 0 0 1 1-1h3.5a1 1 0 0 1 1 1c0 1.25.2 2.45.57 3.57a1 1 0 0 1-.25 1z"/></svg>
        080-4471-2093</p>
      <p class="fax">FAX 080-4471-2093</p>
    </div>
    <p class="org">株式会社ミナトラボ<small>福岡市博多区竹下緑町5-8-3</small><small>福岡市博多区竹下緑町5-8-3</small></p>
    <span class="org-mark"></span>
  </footer>
</main>
</body>
</html>
```